brisk-vale.com Real Estate, Investment, Financial corporate

Real Estate, Investment, Financial corporate looking site. Show present a professional firm, with an elegant display. Please see the attached file which includes the logo, palette and fonts.
Updates

We just starting the brief today. ( logo was delayed)

Target Market(s)

Investors, Corporate , B2b

Industry/Entity Type

real-estate investments

Number of Pages Required

3 page

Requirements
Must have
• Dazzling Homepage
Nice to have
• paralex

```html
<!DOCTYPE html>
<html lang="en">
<head>
<meta charset="utf-8">
<title>Brisk Vale Group — Property Investment Company</title>
<link href="https://fonts.googleapis.com/css2?family=Josefin+Sans:wght@400;600&family=Libre+Baskerville:wght@400;700&family=Lato:wght@400;700&display=swap" rel="stylesheet">
<style>
:root{
  --ink:#262626;
  --ink-deep:#1c1c1c;
  --peach:#f6cf98;
  --cream:#fdf5ea;
  --gold:#c8924a;
  --navy:#1f2340;
  --white:#ffffff;
  --muted:#555;
  --grey:#9a9a9a;
}
*{box-sizing:border-box;margin:0;padding:0}
html,body{width:1200px;height:5133px;overflow:hidden}
body{position:relative;background:var(--ink);font-family:"Lato",sans-serif;color:var(--ink)}
.abs{position:absolute}
.serif{font-family:"Libre Baskerville",serif;font-weight:700}
.sans{font-family:"Josefin Sans",sans-serif}
.btn{position:absolute;display:flex;align-items:center;justify-content:center;border-radius:22px;font-family:"Josefin Sans",sans-serif;font-size:14px;letter-spacing:.5px}
.btn-peach{background:var(--peach);color:var(--ink)}
.btn-navy{background:var(--navy);color:var(--white)}

/* header */
.site-header{top:0;left:0;width:1200px;height:134px;background:var(--ink)}
.brand{left:74px;top:26px;display:flex;align-items:center;gap:12px}
.brand-mark{width:22px;height:22px;background:var(--peach)}
.brand-name{font-family:"Libre Baskerville",serif;font-weight:400;font-size:28px;color:var(--peach)}
.nav{left:484px;top:62px;display:flex;gap:0}
.nav a{position:absolute;top:0;font-family:"Josefin Sans",sans-serif;font-size:14px;color:var(--white);text-decoration:none;white-space:nowrap}
.nav a.active{font-weight:600}
.nav a.active::after{content:"";position:absolute;left:0;right:0;top:26px;height:2px;background:var(--white)}
.contact-btn{left:960px;top:48px;width:166px;height:44px;border-radius:22px;background:var(--grey);overflow:hidden}
.contact-btn span{position:absolute;left:0;top:0;width:126px;height:44px;border-radius:22px;background:var(--peach);display:flex;align-items:center;justify-content:center;font-family:"Josefin Sans",sans-serif;font-size:13px;letter-spacing:.5px}

/* hero */
.hero{top:134px;left:0;width:1200px;height:716px;overflow:hidden}
.hero-photo{position:absolute;inset:0;background:linear-gradient(160deg,#c9d3dc 0%,#8ea3b8 30%,#3d5b86 55%,#b9c3c7 80%,#9aa7b2 100%)}
.hero-title{left:74px;top:290px;font-size:27px;line-height:40px;letter-spacing:2px;color:var(--white)}
.hero-sub{left:76px;top:374px;width:360px;font-size:12px;line-height:15px;color:var(--white)}
.search-panel{left:752px;top:128px;width:368px;height:448px;background:var(--ink)}
.search-head{left:742px;top:142px;width:370px;height:80px;background:var(--peach);display:flex;align-items:center;justify-content:center;text-align:center;font-size:22px;line-height:30px;letter-spacing:2px;color:var(--ink)}
.search-label{left:800px;font-family:"Josefin Sans",sans-serif;font-size:12px;font-weight:600;color:var(--white);letter-spacing:.5px}
.search-select{left:800px;width:256px;height:48px;background:var(--cream);font-family:"Josefin Sans",sans-serif;font-size:13px;color:var(--ink);display:flex;align-items:center;justify-content:space-between;padding:0 14px;letter-spacing:.5px}
.search-btn{left:800px;top:458px;width:256px;height:52px;background:var(--peach);display:flex;align-items:center;justify-content:center;font-family:"Josefin Sans",sans-serif;font-size:13px;font-weight:600;letter-spacing:1px}
.slide-index{right:0;font-family:"Josefin Sans",sans-serif;font-size:12px;color:var(--white);width:30px;text-align:center}

/* services */
.service{top:950px;width:250px;height:246px;background:var(--cream);text-align:center}
.service-icon{position:absolute;left:82px;top:28px;width:86px;height:86px;border-radius:50%;background:#e9dccb}
.service h3{position:absolute;left:0;right:0;top:134px;font-family:"Josefin Sans",sans-serif;font-weight:400;font-size:18px;letter-spacing:1.5px}
.service p{position:absolute;left:24px;right:24px;top:170px;font-size:12px;line-height:19px;color:var(--muted)}
.corner{position:absolute;width:60px;height:60px;border-color:var(--peach);border-style:solid}

/* welcome */
.welcome-photo{left:114px;top:1298px;width:448px;height:508px;background:linear-gradient(135deg,#6f7f94 0%,#b9b4ad 45%,#ddd6cc 70%,#8b8076 100%)}
.eyebrow{left:614px;top:1308px;font-family:"Josefin Sans",sans-serif;font-weight:600;font-size:17px;color:var(--peach);letter-spacing:1px}
.welcome-title{left:614px;top:1336px;font-size:28px;color:var(--white);letter-spacing:1px}
.rule{left:614px;top:1384px;width:176px;height:2px;background:var(--peach)}
.welcome-copy{left:614px;top:1404px;width:460px;font-size:12px;line-height:22px;color:var(--white)}
.welcome-copy p{margin-bottom:22px}

/* investment */
.invest-band{top:1910px;left:0;width:1200px;height:416px;background:var(--peach)}
.section-title{font-size:28px;letter-spacing:.5px}
.arrow-btn{width:40px;height:40px;border-radius:50%;display:flex;align-items:center;justify-content:center}
.property{top:2054px;width:340px;height:560px;background:var(--cream)}
.property-photo{position:absolute;left:0;top:0;width:100%;height:276px}
.property .loc{position:absolute;left:24px;top:296px;font-size:12px;color:var(--peach)}
.property h3{position:absolute;left:24px;top:316px;font-family:"Libre Baskerville",serif;font-size:17px;line-height:24px;letter-spacing:1px}
.property .price{position:absolute;left:24px;top:376px;font-family:"Josefin Sans",sans-serif;font-weight:600;font-size:19px;color:var(--gold);letter-spacing:.5px}
.property ul{position:absolute;left:24px;top:404px;list-style:none;font-size:12px;line-height:22px}
.property li{display:flex;align-items:center;gap:8px}
.property .btn{left:24px;top:490px;width:164px;height:44px}

/* testimonials */
.testimonial{top:2812px;width:338px;height:302px;background:var(--cream);text-align:center}
.quote-mark{position:absolute;left:16px;top:-14px;width:30px;height:30px;border-radius:50%;background:var(--peach);font-family:"Libre Baskerville",serif;font-size:18px;line-height:34px;color:var(--ink)}
.avatar{position:absolute;left:124px;top:30px;width:90px;height:90px;border-radius:50%;background:radial-gradient(circle,#d9c6b4,#8c8f96)}
.testimonial h4{position:absolute;left:0;right:0;top:138px;font-family:"Libre Baskerville",serif;font-size:15px}
.testimonial .role{position:absolute;left:0;right:0;top:162px;font-family:"Libre Baskerville",serif;font-size:11px;color:var(--grey)}
.testimonial p{position:absolute;left:40px;right:40px;top:190px;font-size:12px;line-height:16px;color:var(--muted)}
.stars{position:absolute;left:0;right:0;top:250px;color:var(--gold);font-size:12px;letter-spacing:4px}

/* banner */
.banner{top:3240px;left:0;width:1200px;height:492px;background:linear-gradient(100deg,#a7c4dc 0%,#7fa4c6 35%,#5a7fa7 55%,#3a3f47 75%,#c9ccd0 100%)}
.banner-title{left:74px;top:136px;font-size:28px;line-height:38px;letter-spacing:2px;color:var(--ink)}
.banner-sub{left:76px;top:268px;width:300px;font-size:12px;line-height:15px;color:var(--ink)}

/* blog */
.post{top:3870px;width:338px;height:392px;background:var(--cream)}
.post-photo{position:absolute;left:10px;top:10px;right:10px;height:210px}
.post h4{position:absolute;left:14px;top:240px;font-family:"Libre Baskerville",serif;font-size:13px}
.post .meta{position:absolute;left:14px;top:266px;font-size:13px;display:flex;gap:12px;align-items:center;color:#333}
.post .meta span{display:flex;align-items:center;gap:5px}
.post p{position:absolute;left:14px;right:14px;top:292px;font-size:12px;line-height:17px;color:var(--muted)}
.post svg.go{position:absolute;left:14px;top:362px}

/* contact */
.field{height:40px;background:var(--white);border-radius:20px;font-size:11px;color:#555;padding:14px 22px}
.field-message{left:260px;top:4496px;width:700px;height:124px;border-radius:20px;background:var(--white);font-size:11px;color:#555;padding:14px 22px}

/* footer */
.footer{top:4760px;left:0;width:1200px;height:310px;background:var(--peach)}
.footer h5{position:absolute;top:92px;font-family:"Libre Baskerville",serif;font-size:13px;letter-spacing:.5px}
.footer ul{position:absolute;top:138px;list-style:none;font-family:"Josefin Sans",sans-serif;font-size:13px;line-height:18px;color:var(--ink)}
.contact-line{position:absolute;display:flex;gap:10px;font-size:13px;line-height:16px}
.newsletter-input{position:absolute;left:878px;top:160px;width:248px;height:30px;border-radius:15px;background:var(--white);font-size:11px;font-style:italic;padding:9px 20px}
.newsletter-btn{position:absolute;left:878px;top:208px;width:248px;height:32px;border-radius:16px;background:var(--ink);color:var(--white);font-size:11px;display:flex;align-items:center;justify-content:center;letter-spacing:.5px}
.legal{top:5070px;left:0;width:1200px;height:63px;background:var(--ink-deep)}
.social{position:absolute;top:16px;width:32px;height:32px;border-radius:50%;background:var(--peach)}
</style>
</head>
<body>

<!-- Header -->
<header class="abs site-header">
  <div class="abs brand"><span class="brand-mark"></span><span class="brand-name">Brisk Vale</span></div>
  <nav class="abs nav">
    <a class="active" style="left:0">Home</a>
    <a style="left:86px">About us</a>
    <a style="left:194px">Invesment</a>
    <a style="left:314px">Finance</a>
    <a style="left:416px">Blog</a>
  </nav>
  <div class="abs contact-btn"><span>CONTACT US</span>
    <svg class="abs" style="left:134px;top:15px" width="24" height="14" viewBox="0 0 24 14"><path d="M0 7h22M16 1l6 6-6 6" fill="none" stroke="#fff" stroke-width="1.5"/></svg>
  </div>
</header>

<!-- Hero -->
<section class="abs hero">
  <div class="hero-photo" role="img" aria-label="Upward view of a glass and steel office tower against a cloudy sky"></div>
  <h1 class="abs serif hero-title">PROPERTY<br>INVESMENT COMPANY</h1>
  <p class="abs hero-sub">Lorem Ipsum is a simply dummy text of the print and industry Lorem Ipsum has been the industry's</p>
  <div class="btn btn-navy" style="left:74px;top:422px;width:166px;height:40px">Read More</div>

  <div class="abs search-panel"></div>
  <div class="abs serif search-head">FIND YOUR IDEAL<br>INVESMENT PROPERTY</div>
  <div class="abs search-label" style="top:252px">TYPE OF INVESTMENT</div>
  <div class="abs search-select" style="top:278px"><span>COMMERICAL</span><span>&#x2228;</span></div>
  <div class="abs search-label" style="top:346px">TYPE OF INVESTMENT</div>
  <div class="abs search-select" style="top:370px"><span>WASHINGTON, DC</span><span>&#x2228;</span></div>
  <div class="abs search-btn">SEARCH INVESTMENT</div>
  <svg class="abs" style="left:752px;top:540px" width="370" height="40" viewBox="0 0 370 40"><polygon points="0,40 370,0 370,12 0,40" fill="#f6cf98"/></svg>

  <svg class="abs" style="left:1160px;top:286px" width="40" height="26" viewBox="0 0 40 26"><polygon points="10,0 40,0 40,26 10,26 0,13" fill="#f6cf98"/><text x="24" y="17" font-family="Josefin Sans" font-size="12" fill="#262626" text-anchor="middle">2</text></svg>
  <div class="abs slide-index" style="top:334px">3</div>
  <div class="abs slide-index" style="top:362px">4</div>

  <svg class="abs" style="left:0;top:616px" width="1200" height="100" viewBox="0 0 1200 100"><polygon points="0,30 560,0 600,100 0,100" fill="#f6cf98"/><polygon points="0,70 600,28 1200,46 1200,100 0,100" fill="#262626"/></svg>
  <svg class="abs" style="left:578px;top:626px" width="44" height="72" viewBox="0 0 44 72"><rect x="4" y="2" width="36" height="68" rx="18" fill="#fff" stroke="#262626" stroke-width="2"/><path d="M22 14v40M15 47l7 8 7-8" fill="none" stroke="#262626" stroke-width="2"/></svg>
</section>

<!-- Services -->
<section>
  <article class="abs service" style="left:74px"><div class="service-icon" role="img" aria-label="Finance icon: house with coins"></div><h3>FINANCE</h3><p>Lorem Ipsum is simply dummy setting industry.</p></article>
  <article class="abs service" style="left:342px"><div class="service-icon" role="img" aria-label="Investment icon: person with rising bar chart"></div><h3>INVESTMENT</h3><p>Lorem Ipsum is simply dummy setting industry.</p>
    <span class="corner" style="left:0;top:0;border-width:3px 0 0 3px"></span><span class="corner" style="right:0;bottom:0;border-width:0 3px 3px 0"></span></article>
  <article class="abs service" style="left:610px"><div class="service-icon" role="img" aria-label="Fast process icon: signed document"></div><h3>FAST PROCESS</h3><p>Lorem Ipsum is simply dummy setting industry.</p></article>
  <article class="abs service" style="left:876px"><div class="service-icon" role="img" aria-label="Free consulting icon: adviser with speech bubble"></div><h3>FREE CONSULTING</h3><p>Lorem Ipsum is simply dummy setting industry.</p></article>
</section>

<!-- Welcome -->
<section>
  <span class="abs corner" style="left:108px;top:1290px;border-width:4px 0 0 4px;width:50px;height:50px"></span>
  <div class="abs welcome-photo" role="img" aria-label="Handshake over a small model house, pen and contract on a desk"></div>
  <div class="abs eyebrow">Invest for Your Future</div>
  <h2 class="abs serif welcome-title">WELCOME TO BRISK-VALE</h2>
  <div class="abs rule"></div>
  <div class="abs welcome-copy">
    <p>Lorem Ipsum is simply dummy text of the printing and typesetting industry has been the industry's standard dummy text ever since the 1500s,</p>
    <p>when an unknown printer took a galley of type and scrambled it to make a type specimen book. It has survived not only five centuries, but also the leap into electronic typesetting, remaining essentially unchanged. It was popularised in the 1960s</p>
    <p>with the release of Typeline sheets containing Lorem Ipsum passages, and more recently with desktop publishing software like Folio PageMaster including into electronic typesetting, remaining essentially unchanged. It was popularised versions of Lorem Ipsum.</p>
    <p>Lorem Ipsum is simply dummy text of the printing and typesetting industry has been the industry's standard dummy text ever since the 1500s,</p>
  </div>
  <div class="btn btn-peach" style="left:614px;top:1766px;width:166px;height:40px">Read More</div>
</section>

<!-- Investment opportunities -->
<section>
  <div class="abs invest-band"></div>
  <h2 class="abs serif section-title" style="left:378px;top:1970px">INVESTMENT OPPERTUNITY</h2>
  <div class="abs arrow-btn" style="left:1034px;top:1970px;background:var(--cream)"><svg width="18" height="12" viewBox="0 0 18 12"><path d="M18 6H2M7 1 2 6l5 5" fill="none" stroke="#262626" stroke-width="1.6"/></svg></div>
  <div class="abs arrow-btn" style="left:1084px;top:1970px;background:var(--ink)"><svg width="18" height="12" viewBox="0 0 18 12"><path d="M0 6h16M11 1l5 5-5 5" fill="none" stroke="#fff" stroke-width="1.6"/></svg></div>

  <article class="abs property" style="left:74px">
    <div class="property-photo" role="img" aria-label="Modern residential tower with stacked balconies" style="background:linear-gradient(160deg,#dfe6ec,#9fb0bf 50%,#3f4a55)"></div>
    <div class="loc">Los Angeles, California</div><h3>Exclusive Private Gated<br>Residency</h3><div class="price">From $00.00</div>
    <ul><li><svg width="12" height="12" viewBox="0 0 12 12"><circle cx="6" cy="6" r="5" fill="none" stroke="#262626"/><path d="M3.5 6l2 2 3-4" fill="none" stroke="#262626"/></svg>Huge Groth Expected</li><li><svg width="12" height="12" viewBox="0 0 12 12"><circle cx="6" cy="6" r="5" fill="none" stroke="#262626"/><path d="M3.5 6l2 2 3-4" fill="none" stroke="#262626"/></svg>7% Net Return Guatanted for 2 year</li><li><svg width="12" height="12" viewBox="0 0 12 12"><circle cx="6" cy="6" r="5" fill="none" stroke="#262626"/><path d="M3.5 6l2 2 3-4" fill="none" stroke="#262626"/></svg>Golden Center Location</li></ul>
    <div class="btn btn-peach">Read More</div>
  </article>
  <article class="abs property" style="left:432px;width:338px">
    <div class="property-photo" role="img" aria-label="Tall glass apartment tower against pale sky" style="background:linear-gradient(170deg,#eef1f3,#b7c2cb 55%,#5c6670)"></div>
    <div class="loc">Los Angeles, California</div><h3>Exclusive Private Gated<br>Residency</h3><div class="price">From $00.00</div>
    <ul><li><svg width="12" height="12" viewBox="0 0 12 12"><circle cx="6" cy="6" r="5" fill="none" stroke="#262626"/><path d="M3.5 6l2 2 3-4" fill="none" stroke="#262626"/></svg>Huge Groth Expected</li><li><svg width="12" height="12" viewBox="0 0 12 12"><circle cx="6" cy="6" r="5" fill="none" stroke="#262626"/><path d="M3.5 6l2 2 3-4" fill="none" stroke="#262626"/></svg>7% Net Return Guatanted for 2 year</li><li><svg width="12" height="12" viewBox="0 0 12 12"><circle cx="6" cy="6" r="5" fill="none" stroke="#262626"/><path d="M3.5 6l2 2 3-4" fill="none" stroke="#262626"/></svg>Golden Center Location</li></ul>
    <div class="btn btn-peach">Read More</div>
  </article>
  <article class="abs property" style="left:788px;width:338px">
    <div class="property-photo" role="img" aria-label="Blue glass office building corner" style="background:linear-gradient(150deg,#dbe4ea,#4d7fae 50%,#1f4b7a)"></div>
    <div class="loc">Los Angeles, California</div><h3>Exclusive Private Gated<br>Residency</h3><div class="price">From $00.00</div>
    <ul><li><svg width="12" height="12" viewBox="0 0 12 12"><circle cx="6" cy="6" r="5" fill="none" stroke="#262626"/><path d="M3.5 6l2 2 3-4" fill="none" stroke="#262626"/></svg>Huge Groth Expected</li><li><svg width="12" height="12" viewBox="0 0 12 12"><circle cx="6" cy="6" r="5" fill="none" stroke="#262626"/><path d="M3.5 6l2 2 3-4" fill="none" stroke="#262626"/></svg>7% Net Return Guatanted for 2 year</li><li><svg width="12" height="12" viewBox="0 0 12 12"><circle cx="6" cy="6" r="5" fill="none" stroke="#262626"/><path d="M3.5 6l2 2 3-4" fill="none" stroke="#262626"/></svg>Golden Center Location</li></ul>
    <div class="btn btn-peach">Read More</div>
  </article>
</section>

<!-- Testimonials -->
<section>
  <h2 class="abs serif section-title" style="left:0;width:1186px;text-align:center;top:2706px;color:var(--white)">TESTIMONIALS</h2>
  <div class="abs" style="left:0;width:1186px;text-align:center;top:2746px;font-size:11px;color:var(--white)">What Clients say about us</div>
  <article class="abs testimonial" style="left:74px"><div class="quote-mark">&ldquo;</div><div class="avatar" role="img" aria-label="Portrait of client"></div><h4>Martin Cole</h4><div class="role">Creative Director</div><p>Lorem Ipsum simply dummy text printing and typesetting industry simply dummy a psum is simply dummy</p><div class="stars">★★★★★</div></article>
  <article class="abs testimonial" style="left:432px"><div class="quote-mark">&ldquo;</div><div class="avatar" role="img" aria-label="Portrait of client"></div><h4>Elena Marsh</h4><div class="role">Creative Director</div><p>Lorem Ipsum simply dummy text printing and typesetting industry simply dummy a psum is simply dummy</p><div class="stars">★★★★★</div></article>
  <article class="abs testimonial" style="left:788px"><div class="quote-mark">&ldquo;</div><div class="avatar" role="img" aria-label="Portrait of client"></div><h4>Priya Hale</h4><div class="role">Creative Director</div><p>Lorem Ipsum simply dummy text printing and typesetting industry simply dummy a psum is simply dummy</p><div class="stars">★★★★★</div></article>
  <svg class="abs" style="left:584px;top:3172px" width="36" height="10" viewBox="0 0 36 10"><circle cx="5" cy="5" r="3.5" fill="#fff"/><circle cx="18" cy="5" r="3.5" fill="#fff"/><circle cx="31" cy="5" r="3.5" fill="#fff"/></svg>
</section>

<!-- Banner -->
<section class="abs banner" role="img" aria-label="Dark modern apartment building with cantilevered balconies against blue sky">
  <h2 class="abs serif banner-title">We Help Our<br>Investor in our<br>Projects</h2>
  <p class="abs banner-sub">Lorem Ipsum is a simply dummy text of the industry Lorem has been the industry's</p>
  <div class="btn btn-peach" style="left:74px;top:312px;width:166px;height:40px">Read More</div>
</section>

<!-- Blog -->
<section>
  <h2 class="abs serif section-title" style="left:0;width:1188px;text-align:center;top:3804px;color:var(--white)">OUR BLOG</h2>
  <article class="abs post" style="left:74px"><div class="post-photo" role="img" aria-label="City skyline with glass skyscraper at sunset" style="background:linear-gradient(180deg,#b9cde0,#6f7f8f 55%,#8a5a3c)"></div><h4>Blog Title Heading</h4><div class="meta"><span><svg width="12" height="12" viewBox="0 0 12 12"><rect x="1" y="2" width="10" height="9" fill="none" stroke="#333"/><path d="M1 5h10" stroke="#333"/></svg>21/11/2021</span><span><svg width="12" height="12" viewBox="0 0 12 12"><circle cx="6" cy="4" r="2.5" fill="none" stroke="#333"/><path d="M1.5 11.5c0-3 9-3 9 0" fill="none" stroke="#333"/></svg>Martin Cole</span></div><p>Lorem Ipsum is simply dummy text of the print ing and typesetting industry. Lorem Ipsum is has been the industry's</p><svg class="go" width="44" height="10" viewBox="0 0 44 10"><path d="M0 5h42M37 1l5 4-5 4" fill="none" stroke="#262626" stroke-width="1.4"/></svg></article>
  <article class="abs post" style="left:432px;width:334px"><div class="post-photo" role="img" aria-label="Downtown towers in blue haze" style="background:linear-gradient(180deg,#b7d0e3,#4e7390 55%,#1f3b4f)"></div><h4>Blog Title Heading</h4><div class="meta"><span><svg width="12" height="12" viewBox="0 0 12 12"><rect x="1" y="2" width="10" height="9" fill="none" stroke="#333"/><path d="M1 5h10" stroke="#333"/></svg>21/11/2020</span><span><svg width="12" height="12" viewBox="0 0 12 12"><circle cx="6" cy="4" r="2.5" fill="none" stroke="#333"/><path d="M1.5 11.5c0-3 9-3 9 0" fill="none" stroke="#333"/></svg>Martin Cole</span></div><p>Lorem Ipsum is simply dummy text of the print ing and typesetting industry. Lorem Ipsum is has been the industry's</p><svg class="go" width="44" height="10" viewBox="0 0 44 10"><path d="M0 5h42M37 1l5 4-5 4" fill="none" stroke="#262626" stroke-width="1.4"/></svg></article>
  <article class="abs post" style="left:792px;width:334px"><div class="post-photo" role="img" aria-label="Black and white view up between skyscrapers" style="background:linear-gradient(180deg,#e4e4e4,#8a8a8a 50%,#2a2a2a)"></div><h4>Blog Title Heading</h4><div class="meta"><span><svg width="12" height="12" viewBox="0 0 12 12"><rect x="1" y="2" width="10" height="9" fill="none" stroke="#333"/><path d="M1 5h10" stroke="#333"/></svg>21/11/2019</span><span><svg width="12" height="12" viewBox="0 0 12 12"><circle cx="6" cy="4" r="2.5" fill="none" stroke="#333"/><path d="M1.5 11.5c0-3 9-3 9 0" fill="none" stroke="#333"/></svg>Martin Cole</span></div><p>Lorem Ipsum is simply dummy text of the print ing and typesetting industry. Lorem Ipsum is has been the industry's</p><svg class="go" width="44" height="10" viewBox="0 0 44 10"><path d="M0 5h42M37 1l5 4-5 4" fill="none" stroke="#262626" stroke-width="1.4"/></svg></article>
  <div class="btn btn-peach" style="left:518px;top:4292px;width:168px;height:40px">Read More</div>
</section>

<!-- Contact -->
<section>
  <h2 class="abs serif section-title" style="left:0;width:1200px;text-align:center;top:4378px;color:var(--white)">CONTAC US</h2>
  <div class="abs field" style="left:260px;top:4444px;width:230px">Full Name</div>
  <div class="abs field" style="left:496px;top:4444px;width:228px">Email</div>
  <div class="abs field" style="left:730px;top:4444px;width:230px">Phone</div>
  <div class="abs field-message">Message</div>
  <div class="btn btn-peach" style="left:518px;top:4652px;width:168px;height:40px">Send</div>
</section>

<!-- Footer -->
<footer class="abs footer">
  <div class="abs brand" style="top:140px"><span class="brand-mark" style="background:var(--ink)"></span><span class="brand-name" style="color:var(--ink);font-size:30px">Brisk Vale</span></div>
  <h5 style="left:372px">QUICK LINKS</h5>
  <ul style="left:372px"><li>&gt; Home</li><li>&gt; About us</li><li>&gt; Invesment</li><li>&gt; Finance</li><li>&gt; Blog</li><li>&gt; Contact us</li></ul>
  <h5 style="left:578px">CONTACT DETAIL</h5>
  <div class="contact-line" style="left:578px;top:138px"><svg width="12" height="12" viewBox="0 0 12 12"><path d="M2 1l3 0 1 3-1.5 1a7 7 0 0 0 2.5 2.5L8 6l3 1v3c-5 1-10-4-9-9z" fill="#262626"/></svg>555 014 2290</div>
  <div class="contact-line" style="left:578px;top:168px"><svg width="12" height="12" viewBox="0 0 12 12"><rect x="1" y="2.5" width="10" height="7" fill="none" stroke="#262626"/><path d="M1 3l5 4 5-4" fill="none" stroke="#262626"/></svg>info@brisk-vale.com</div>
  <div class="contact-line" style="left:578px;top:198px"><svg width="12" height="14" viewBox="0 0 12 14"><path d="M6 13s-4.5-5-4.5-8a4.5 4.5 0 0 1 9 0c0 3-4.5 8-4.5 8z" fill="#262626"/><circle cx="6" cy="5" r="1.6" fill="#f6cf98"/></svg><span>58 Larch Row<br>#410, Fairmont, GA 30999</span></div>
  <h5 style="left:878px">NEWSLETTER</h5>
  <div class="abs" style="left:878px;top:136px;font-size:12px">Lorem Ipsum is simply dummy printing</div>
  <div class="newsletter-input">Email Address</div>
  <div class="newsletter-btn">SUBSCRIBE</div>
</footer>
<div class="abs legal">
  <div class="abs" style="left:74px;top:26px;font-size:12px;color:var(--white)">Copyright © 2021 <b>BRISK VALE GROUP</b>, All Rights Reserved.</div>
  <span class="social" style="left:950px"></span><span class="social" style="left:998px"></span><span class="social" style="left:1046px"></span><span class="social" style="left:1094px"></span>
</div>

</body>
</html>
```